Corvane Quince Bark Extract Supreme Serum - Product Label

Hi Guys,

I threw up a rough label sketch. Looking to keep the label clean and fresh.

LABEL DIMENSIONS: 4.05 in (Height) x 1.18 in (Diameter)

Industry/Entity Type

Beauty Aid

Font styles to use
Serif

Colors
0255a3
0592cd
6b449b
ffc214

Requirements
Must have
• Velloriant
• S K I N
Nice to have
• We can try purple, gold and black or stick with the blue scheme we have going.

```html
<!DOCTYPE html>
<html lang="en">
<head>
<meta charset="utf-8">
<title>Velloriant Skin – Label Options</title>
<link rel="stylesheet" href="https://fonts.googleapis.com/css2?family=Open+Sans:wght@300;400;600&display=swap">
<style>
  :root{
    --brand-blue:#0255a3;
    --bright-blue:#0592cd;
    --ink:#1b1b1b;
    --band-text:#ffffff;
    --label-bg:#ffffff;
    --page-bg:#ffffff;
    --water-deep:#9fc3e6;
    --water-light:#e6f1fb;
    --rule:#d0d0d0;
  }
  *{box-sizing:border-box;margin:0;padding:0}
  html,body{width:1200px;height:1200px;overflow:hidden;background:var(--page-bg)}
  .sheet{position:relative;width:1200px;height:1200px;font-family:"Open Sans",Arial,sans-serif}
  .option{position:absolute;width:230px;height:330px}
  .option-letter{position:absolute;top:-34px;left:0;font-size:16px;color:var(--ink);font-weight:400}
  .label{position:relative;width:100%;height:100%;background:var(--label-bg);overflow:hidden;box-shadow:0 0 0 1px var(--rule)}
  .brand-name{position:absolute;left:22px;top:20px;font-size:21px;font-weight:600;color:var(--brand-blue);line-height:1.2;z-index:2;white-space:nowrap}
  .product{position:absolute;left:22px;top:62px;width:190px;z-index:2}
  .product-line{font-weight:600;font-size:11px;color:var(--brand-blue);letter-spacing:0.3px;line-height:1.3}
  .range{font-weight:300;font-size:15px;color:var(--bright-blue);line-height:1.3;margin-bottom:6px}
  .boxes{display:flex;flex-direction:column;align-items:flex-start}
  .box-outline,.box-fill{display:inline-block;font-size:13.5px;font-weight:600;padding:0 6px;line-height:20px;white-space:nowrap}
  .box-outline{border:1.5px solid var(--brand-blue);color:var(--brand-blue)}
  .box-fill{background:var(--brand-blue);color:#fff;border:1.5px solid var(--brand-blue);margin-top:1px}
  .size-band{position:absolute;left:0;right:0;bottom:0;height:38px;background:var(--brand-blue);color:var(--band-text);
    font-size:12px;display:flex;align-items:center;justify-content:center;z-index:3}
  .water{position:absolute;z-index:1}
  .water--drop{left:60px;right:0;top:170px;height:122px;background:radial-gradient(ellipse at 60% 75%,var(--water-deep) 0%,var(--water-light) 45%,rgba(255,255,255,0) 75%)}
  .water--swirl{left:60px;right:0;top:50px;height:140px;background:radial-gradient(ellipse at 55% 45%,var(--water-deep) 0%,var(--water-light) 45%,rgba(255,255,255,0) 72%)}
  .water--splash{left:100px;right:0;top:50px;height:140px;background:radial-gradient(ellipse at 65% 40%,#b7cfe6 0%,var(--water-light) 40%,rgba(255,255,255,0) 70%)}
  .water--wave{left:0;right:0;top:50px;bottom:38px;background:radial-gradient(ellipse at 80% 35%,var(--water-deep) 0%,var(--water-light) 40%,rgba(255,255,255,0) 68%)}
  .water--sphere{left:90px;right:0;top:50px;height:150px;background:radial-gradient(circle at 60% 45%,var(--water-deep) 0%,var(--water-light) 42%,rgba(255,255,255,0) 66%)}
  .product--low{top:192px}
  .theme-black .box-outline{border-color:var(--ink);color:var(--ink)}
  .theme-black .box-fill{background:var(--ink);border-color:var(--ink)}
  .theme-cyan .box-outline{border-color:var(--ink);color:var(--ink)}
  .theme-cyan .box-fill{background:var(--bright-blue);border-color:var(--bright-blue)}
  .theme-mixed .range{color:var(--ink)}
  .theme-mixed .box-outline{border-color:var(--bright-blue);color:var(--bright-blue)}
  .theme-mixed .box-fill{background:var(--ink);border-color:var(--ink)}
</style>
</head>
<body>
<main class="sheet">

  <section class="option" style="left:166px;top:245px">
    <span class="option-letter">A</span>
    <div class="label">
      <div class="brand-name">Velloriant Skin</div>
      <div class="product">
        <div class="product-line">CORVANE QUINCE</div>
        <div class="range">BARK EXTRACT</div>
        <div class="boxes"><span class="box-outline">Revitalizing</span><span class="box-fill">Face Serum</span></div>
      </div>
      <div class="water water--drop" role="img" aria-label="Water droplet falling into a splash"></div>
      <div class="size-band">1 fl. oz / 30ml</div>
    </div>
  </section>

  <section class="option theme-black" style="left:485px;top:245px">
    <span class="option-letter">B</span>
    <div class="label">
      <div class="brand-name">Velloriant Skin</div>
      <div class="water water--swirl" role="img" aria-label="Swirling clear water splash"></div>
      <div class="product product--low">
        <div class="product-line">CORVANE QUINCE</div>
        <div class="range">BARK EXTRACT</div>
        <div class="boxes"><span class="box-outline">Revitalizing</span><span class="box-fill">Face Serum</span></div>
      </div>
      <div class="size-band">1 fl. oz / 30ml</div>
    </div>
  </section>

  <section class="option theme-cyan" style="left:804px;top:245px">
    <span class="option-letter">C</span>
    <div class="label">
      <div class="brand-name">Velloriant Skin</div>
      <div class="water water--splash" role="img" aria-label="Rising water splash with droplets"></div>
      <div class="product product--low">
        <div class="product-line">CORVANE QUINCE</div>
        <div class="range">BARK EXTRACT</div>
        <div class="boxes"><span class="box-outline">Revitalizing</span><span class="box-fill">Face Serum</span></div>
      </div>
      <div class="size-band">1 fl. oz / 30ml</div>
    </div>
  </section>

  <section class="option theme-mixed" style="left:166px;top:830px">
    <span class="option-letter">D</span>
    <div class="label">
      <div class="water water--wave" role="img" aria-label="Curving wave of clear water"></div>
      <div class="brand-name">Velloriant Skin</div>
      <div class="product product--low">
        <div class="product-line">CORVANE QUINCE</div>
        <div class="range">BARK EXTRACT</div>
        <div class="boxes"><span class="box-outline">Revitalizing</span><span class="box-fill">Face Serum</span></div>
      </div>
      <div class="size-band">1 fl. oz / 30ml</div>
    </div>
  </section>

  <section class="option theme-mixed" style="left:485px;top:830px">
    <span class="option-letter">E</span>
    <div class="label">
      <div class="water water--wave" role="img" aria-label="Curving wave of clear water"></div>
      <div class="brand-name">Velloriant Skin</div>
      <div class="product product--low">
        <div class="product-line">CORVANE QUINCE</div>
        <div class="range">BARK EXTRACT</div>
        <div class="boxes"><span class="box-outline">Revitalizing</span><span class="box-fill">Face Serum</span></div>
      </div>
      <div class="size-band">1 fl. oz / 30ml</div>
    </div>
  </section>

  <section class="option theme-black" style="left:804px;top:830px">
    <span class="option-letter">F</span>
    <div class="label">
      <div class="water water--sphere" role="img" aria-label="Splashing sphere of water"></div>
      <div class="brand-name">Velloriant Skin</div>
      <div class="product product--low">
        <div class="product-line">CORVANE QUINCE</div>
        <div class="range">BARK EXTRACT</div>
        <div class="boxes"><span class="box-outline">Revitalizing</span><span class="box-fill">Face Serum</span></div>
      </div>
      <div class="size-band">1 fl. oz / 30ml</div>
    </div>
  </section>

</main>
</body>
</html>
```